Quilvo Garage Doors Business Card

I need a Business Card for my garage door business:
Quilvo Garage Doors.
please add:
logo
phone number: 855-3-QUILVO
(853-392)

email: service@quilvogaragedoors.com
website: www.quilvogaragedoors.com

The attached image is recommendation ONLY.

```html
<!DOCTYPE html>
<html lang="en">
<head>
<meta charset="utf-8">
<title>Quilvo Garage Doors – Business Card</title>
<link rel="stylesheet" href="https://fonts.googleapis.com/css2?family=Open+Sans:wght@400;600;700&display=swap">
<style>
  :root {
    --teal: #52c3d0;
    --ink: #1f1f1f;
    --paper: #ffffff;
    --backdrop: #ecebe8;
    --shadow: rgba(0, 0, 0, 0.14);
  }
  * { box-sizing: border-box; margin: 0; padding: 0; }
  html, body {
    width: 1200px;
    height: 900px;
    overflow: hidden;
    background: var(--backdrop);
    font-family: "Open Sans", Arial, sans-serif;
  }
  .canvas {
    position: relative;
    width: 1200px;
    height: 900px;
  }
  .card {
    position: absolute;
    left: 330px;
    width: 540px;
    height: 310px;
    border-radius: 4px;
    box-shadow: 0 8px 24px var(--shadow);
  }
  .card--front {
    top: 120px;
    background: var(--teal);
    display: flex;
    align-items: center;
    justify-content: center;
  }
  .card--back {
    top: 470px;
    background: var(--paper);
  }
  .brand-name {
    font-weight: 600;
    line-height: 1.05;
  }
  .card--front .brand-name {
    color: var(--paper);
    font-size: 38px;
  }
  .contact {
    position: absolute;
    left: 290px;
    top: 42px;
    color: var(--ink);
  }
  .contact__name {
    color: var(--teal);
    font-weight: 700;
    font-size: 17px;
  }
  .contact__title {
    font-size: 12px;
    margin-top: 1px;
  }
  .contact__list {
    list-style: none;
    margin-top: 22px;
    font-size: 12.5px;
  }
  .contact__list li {
    display: flex;
    align-items: center;
    gap: 9px;
    margin-bottom: 6px;
  }
  .contact__icon {
    width: 11px;
    height: 11px;
    flex: none;
  }
  .signature {
    position: absolute;
    left: 36px;
    bottom: 40px;
    display: flex;
    align-items: center;
    gap: 16px;
  }
  .signature__mark {
    width: 62px;
    height: 62px;
    border-radius: 50%;
    background: var(--teal);
  }
  .card--back .brand-name {
    color: var(--ink);
    font-size: 27px;
  }
</style>
</head>
<body>
<main class="canvas">
  <section class="card card--front" aria-label="Card front">
    <p class="brand-name">Quilvo<br>Garage Doors</p>
  </section>

  <section class="card card--back" aria-label="Card back">
    <div class="contact">
      <p class="contact__name">Daniel Marsh</p>
      <p class="contact__title">Managing Director</p>
      <ul class="contact__list">
        <li>
          <svg class="contact__icon" viewBox="0 0 12 12" aria-hidden="true"><path fill="#52c3d0" d="M2.4 0.6l1.9 2.2-1 1.3c.7 1.5 1.9 2.7 3.4 3.4l1.3-1 2.2 1.9-.9 2c-4.9-.3-8.5-3.9-8.8-8.8z"/></svg>
          <span>855-3-QUILVO</span>
        </li>
        <li>
          <svg class="contact__icon" viewBox="0 0 12 12" aria-hidden="true"><rect x="0.5" y="2" width="11" height="8" fill="#52c3d0"/><path d="M0.5 2.3L6 6.4l5.5-4.1" fill="none" stroke="#fff" stroke-width="1"/></svg>
          <span>service@quilvogaragedoors.com</span>
        </li>
        <li>
          <svg class="contact__icon" viewBox="0 0 12 12" aria-hidden="true"><circle cx="6" cy="6" r="5.5" fill="#52c3d0"/><path d="M0.5 6h11M6 0.5c-2.4 3-2.4 8 0 11M6 0.5c2.4 3 2.4 8 0 11" fill="none" stroke="#fff" stroke-width="0.8"/></svg>
          <span>www.quilvogaragedoors.com</span>
        </li>
      </ul>
    </div>

    <div class="signature">
      <span class="signature__mark" aria-hidden="true"></span>
      <p class="brand-name">Quilvo<br>Garage Doors</p>
    </div>
  </section>
</main>
</body>
</html>
```